Whitmore Properties
business cards, stationery
Can you please extend the contest ....
can you please extend the contest?
@vElpo - we like the black and gold card in #16 but do not like the gold and white stationary. We would like more black in the stationary with gold being the accent with more focus at the top of the stationary.
The font used in our logo is "Trajanpro" both regular and bold.
kindly tell the font name which is used in your logo ...

```html
<!DOCTYPE html>
<html lang="en">
<head>
<meta charset="utf-8">
<title>Whitmore Properties – Business Cards</title>
<link rel="stylesheet" href="https://fonts.googleapis.com/css2?family=Cinzel:wght@400;700&family=Open+Sans:wght@400;700&display=swap">
<style>
  :root {
    --backdrop: #8e8e8e;
    --black: #070707;
    --white: #ffffff;
    --orange: #f39a1c;
    --orange-deep: #e0700e;
    --gold-light: #fbd13a;
    --grey-card: #9a9a9a;
    --ink: #1a1a1a;
  }
  * { margin: 0; padding: 0; box-sizing: border-box; }
  html, body { width: 1200px; height: 792px; overflow: hidden; background: var(--backdrop); }
  .sheet { position: relative; width: 1200px; height: 792px; }
  .card {
    position: absolute; width: 513px; height: 315px; overflow: hidden;
    box-shadow: 0 2px 8px rgba(0,0,0,.35);
  }
  .card--front-a { left: 80px; top: 80px; background: var(--black); }
  .card--back-grey { left: 634px; top: 80px; background: radial-gradient(ellipse at 50% 45%, #b4b4b4 0%, #8a8a8a 80%); }
  .card--back-orange { left: 80px; top: 419px; background: radial-gradient(ellipse at 50% 50%, var(--gold-light) 0%, var(--orange) 45%, var(--orange-deep) 100%); }
  .card--front-b { left: 634px; top: 419px; background: var(--black); }
  .card svg.sweep { position: absolute; inset: 0; width: 513px; height: 315px; }

  .holder-name {
    position: absolute; font-family: "Open Sans", sans-serif; font-weight: 700;
    font-size: 17px; color: var(--white);
  }
  .card--front-a .holder-name { left: 48px; top: 60px; }
  .card--front-b .holder-name { left: 340px; top: 80px; }

  .brand { position: absolute; display: flex; align-items: center; gap: 10px; }
  .brand__mark { width: 26px; height: 26px; background: var(--orange); flex: none; }
  .brand__name {
    font-family: "Cinzel", serif; font-weight: 700; color: var(--white);
    font-size: 22px; line-height: 1.05; letter-spacing: .5px;
  }
  .card--front-a .brand { left: 262px; top: 62px; }
  .card--front-b .brand { left: 44px; top: 46px; }

  .brand-faint {
    position: absolute; inset: 0; display: flex; align-items: center; justify-content: center;
    font-family: "Cinzel", serif; font-weight: 700; font-size: 34px; line-height: 1.1;
    text-align: center; letter-spacing: 1px;
  }
  .card--back-grey .brand-faint { color: rgba(255,255,255,.16); }
  .card--back-orange .brand-faint { color: rgba(255,255,255,.18); }

  .contact { position: absolute; list-style: none; font-family: "Open Sans", sans-serif; font-size: 11px; color: var(--ink); line-height: 1.45; }
  .card--front-a .contact { left: 40px; top: 208px; }
  .card--front-b .contact { left: 40px; top: 196px; }
  .contact li { display: flex; align-items: flex-start; gap: 6px; }
  .contact .icon { width: 11px; height: 11px; flex: none; margin-top: 2px; }
  .contact .address span { display: block; }
</style>
</head>
<body>
<main class="sheet">

  <section class="card card--front-a" aria-label="Business card front, layout A">
    <svg class="sweep" viewBox="0 0 513 315" aria-hidden="true">
      <defs>
        <radialGradient id="glowA" cx="0.32" cy="0.82" r="0.75">
          <stop offset="0" stop-color="#fcd23a"/>
          <stop offset="0.35" stop-color="#f39a1c"/>
          <stop offset="0.7" stop-color="#c8650c"/>
          <stop offset="1" stop-color="#070707"/>
        </radialGradient>
      </defs>
      <path d="M0,168 C160,182 340,160 513,92 L513,315 L0,315 Z" fill="url(#glowA)"/>
      <path d="M0,168 C160,182 340,160 513,92" fill="none" stroke="#ffffff" stroke-width="3"/>
    </svg>
    <p class="holder-name">Nolan Ashby</p>
    <div class="brand">
      <span class="brand__mark"></span>
      <p class="brand__name">WHITMORE<br>PROPERTIES</p>
    </div>
    <ul class="contact">
      <li class="address">
        <svg class="icon" viewBox="0 0 12 12"><circle cx="6" cy="6" r="6" fill="#1a1a1a"/><path d="M6 2.5a2 2 0 0 0-2 2c0 1.6 2 4.5 2 4.5s2-2.9 2-4.5a2 2 0 0 0-2-2z" fill="#f39a1c"/></svg>
        <div><span>4827 Harbor Crest Lane</span><span>Millbrook, California 95612</span></div>
      </li>
      <li>
        <svg class="icon" viewBox="0 0 12 12"><circle cx="6" cy="6" r="6" fill="#1a1a1a"/><path d="M4 3l1.2 1.4-.6.8c.4.9 1.1 1.6 2 2l.8-.6L9 7.8 8.2 9C5.8 8.8 3.2 6.2 3 3.8z" fill="#f39a1c"/></svg>
        <span>(555) 218-3047</span>
      </li>
      <li>
        <svg class="icon" viewBox="0 0 12 12"><circle cx="6" cy="6" r="6" fill="#1a1a1a"/><rect x="3" y="3.5" width="6" height="5" fill="#f39a1c"/><rect x="4" y="4.5" width="4" height="1" fill="#1a1a1a"/></svg>
        <span>(555) 630-9142</span>
      </li>
      <li>
        <svg class="icon" viewBox="0 0 12 12"><circle cx="6" cy="6" r="6" fill="#1a1a1a"/><rect x="3" y="4" width="6" height="4.2" fill="#f39a1c"/><path d="M3 4l3 2.4L9 4" fill="none" stroke="#1a1a1a" stroke-width=".8"/></svg>
        <span>nolan@whitmoreproperties.net</span>
      </li>
    </ul>
  </section>

  <section class="card card--back-grey" aria-label="Business card back, grey">
    <p class="brand-faint">WHITMORE<br>PROPERTIES</p>
  </section>

  <section class="card card--back-orange" aria-label="Business card back, orange">
    <p class="brand-faint">WHITMORE<br>PROPERTIES</p>
  </section>

  <section class="card card--front-b" aria-label="Business card front, layout B">
    <svg class="sweep" viewBox="0 0 513 315" aria-hidden="true">
      <defs>
        <radialGradient id="glowB" cx="0.3" cy="0.85" r="0.8">
          <stop offset="0" stop-color="#fcd23a"/>
          <stop offset="0.35" stop-color="#f39a1c"/>
          <stop offset="0.72" stop-color="#c8650c"/>
          <stop offset="1" stop-color="#070707"/>
        </radialGradient>
      </defs>
      <path d="M0,140 C150,150 360,190 513,290 L513,315 L0,315 Z" fill="url(#glowB)"/>
      <path d="M0,140 C150,150 360,190 513,290" fill="none" stroke="#ffffff" stroke-width="3"/>
    </svg>
    <div class="brand">
      <span class="brand__mark"></span>
      <p class="brand__name">WHITMORE<br>PROPERTIES</p>
    </div>
    <p class="holder-name">Nolan Ashby</p>
    <ul class="contact">
      <li class="address">
        <svg class="icon" viewBox="0 0 12 12"><circle cx="6" cy="6" r="6" fill="#1a1a1a"/><path d="M6 2.5a2 2 0 0 0-2 2c0 1.6 2 4.5 2 4.5s2-2.9 2-4.5a2 2 0 0 0-2-2z" fill="#f39a1c"/></svg>
        <div><span>4827 Harbor Crest Lane</span><span>Millbrook, California 95612</span></div>
      </li>
      <li>
        <svg class="icon" viewBox="0 0 12 12"><circle cx="6" cy="6" r="6" fill="#1a1a1a"/><path d="M4 3l1.2 1.4-.6.8c.4.9 1.1 1.6 2 2l.8-.6L9 7.8 8.2 9C5.8 8.8 3.2 6.2 3 3.8z" fill="#f39a1c"/></svg>
        <span>(555) 218-3047</span>
      </li>
      <li>
        <svg class="icon" viewBox="0 0 12 12"><circle cx="6" cy="6" r="6" fill="#1a1a1a"/><rect x="3" y="3.5" width="6" height="5" fill="#f39a1c"/><rect x="4" y="4.5" width="4" height="1" fill="#1a1a1a"/></svg>
        <span>(555) 630-9142</span>
      </li>
      <li>
        <svg class="icon" viewBox="0 0 12 12"><circle cx="6" cy="6" r="6" fill="#1a1a1a"/><rect x="3" y="4" width="6" height="4.2" fill="#f39a1c"/><path d="M3 4l3 2.4L9 4" fill="none" stroke="#1a1a1a" stroke-width=".8"/></svg>
        <span>nolan@whitmoreproperties.net</span>
      </li>
    </ul>
  </section>

</main>
</body>
</html>
```